Sparrowgate Petals Website v.1 - attract floral shop franchisees

I need a simple information website for my new business. We are a franchisor of flower shops. The overall purpose of the website is to promote the company and the service, especially to potential franchisees and retailers. Only about 4 pages are required including homepage, About, For Supermarkets, For Franchisees, and Contact. No special functions are required except the site will have two separate inquiry forms that must be filled out online and submitted via automated email. Similarly, an email form should be linked from the Contact page. I have a logo and business cards designed by ArtQuarry, and I would like the site to have a consistent color scheme and style. The key to design will be to express the joy and love associated with flowers and floral bouquets.
IMPORTANT - I will be exporting the website design to Wordpress CMS in a site hosted by HostNimbus. For smooth integration into WordPress hosted by HostNimbus, the designer should build the site using a WordPress-friendly format. Ideally, they should use HTML, CSS, and PHP. Creating a custom theme or using a page builder that exports to WordPress-compatible files is best. This ensures the site can be easily imported and managed within WordPress.

Target Market(s)

Potential franchisees (existing florists or creative types who might like to own a floral business) and supermarkets who might want us to run their floral department

Industry/Entity Type

Floral retailing

Requirements
Must have
• A brand theme that is beautiful, consistent throughout and builds on the logo design
Nice to have
• Show gender and ethnic diversity in customers and florists. Pictures of happy florists (for franchisees) and pictures of amazing floral department displays (for supermarkets)

```html
<!DOCTYPE html>
<html lang="en">
<head>
<meta charset="utf-8">
<title>Sparrowgate Petals</title>
<link href="https://fonts.googleapis.com/css2?family=Inter:wght@400;500;600;700&family=Montserrat:wght@700;800&display=swap" rel="stylesheet">
<style>
:root{
  --bg:#fdf7f6;
  --ink:#1d1d1d;
  --muted:#9a9a9a;
  --orange:#eea22a;
  --green:#1e8f3e;
  --rule:#bdb6b3;
}
*{margin:0;padding:0;box-sizing:border-box}
html,body{width:810px;height:1200px;overflow:hidden;background:var(--bg)}
body{position:relative;font-family:'Inter',sans-serif;color:var(--ink)}
.abs{position:absolute}
.icon{position:absolute;width:16px;height:16px}
.brand{position:absolute;left:0;width:810px;top:20px;display:flex;justify-content:center;align-items:center;gap:6px}
.brand-dot{width:14px;height:14px;border-radius:50%;background:var(--green)}
.brand-name{font-size:15px;font-weight:600;color:var(--orange);letter-spacing:.3px}
.nav-rule{left:213px;top:63px;width:384px;height:1px;background:var(--rule)}
.nav{position:absolute;top:70px;left:0;width:810px;font-size:8.5px}
.nav a{position:absolute;color:var(--ink);text-decoration:none;transform:translateX(-50%);white-space:nowrap}
.photo{position:absolute}
.hero-photo{left:273px;top:106px;width:284px;height:291px;background:linear-gradient(135deg,#c9b53a,#d8553a 45%,#e07a2e 70%,#7a6a3a)}
.hero-circle{left:528px;top:249px;width:176px;height:176px;border-radius:50%;background:radial-gradient(circle,#f2b5c0,#7ea46a 70%,#d9d6d2)}
.deco-right{left:761px;top:116px;width:49px;height:194px;background:linear-gradient(180deg,#f5c830,#2f8a3e 40%,#e0508a 70%,#2f7a3a);opacity:.55;border-radius:30px 0 0 30px}
.bee-trail{left:27px;top:173px;width:76px;height:140px;background:linear-gradient(180deg,#2f9a4a,#e8f1ea);opacity:.35;border-radius:40px}
.hero-title{left:86px;top:214px;font-family:'Montserrat',sans-serif;font-weight:800;font-size:33px;line-height:35px;letter-spacing:1px;color:#c8451f}
.btn{position:absolute;width:92px;height:29px;background:var(--orange);color:#fff;font-size:8.5px;font-weight:600;display:flex;align-items:center;justify-content:center;border-radius:2px}
.hero-note{left:568px;top:181px;width:165px;font-size:7px;line-height:10.3px}
.section-title{font-family:'Montserrat',sans-serif;font-weight:700;font-size:22px}
.about-title{left:80px;top:457px}
.about-rule{left:207px;top:471px;width:522px;height:1px;background:var(--orange)}
.next-btn{left:113px;top:607px;width:32px;height:32px;border:1px solid var(--green);border-radius:50%;display:flex;align-items:center;justify-content:center}
.about-photo-a{left:207px;top:512px;width:254px;height:221px;border-radius:3px;background:linear-gradient(135deg,#7a9a5a,#d63a6a 45%,#5a7ab0 80%)}
.about-photo-b{left:475px;top:512px;width:254px;height:221px;border-radius:3px;background:linear-gradient(160deg,#c87aa8,#e0a040 35%,#2a2a2a 60%,#d8402e)}
.body-text{font-size:8.1px;line-height:12.4px}
.body-text strong{color:var(--green);font-weight:600;font-size:9.2px}
.about-text{left:207px;top:745px;width:525px}
.deco-left{left:0;top:702px;width:49px;height:140px;background:linear-gradient(180deg,#e58ac0,#d0308a 60%,#e64aa0);opacity:.6;border-radius:0 30px 30px 0}
.bee-mark{left:605px;top:791px;width:38px;height:27px;background:linear-gradient(90deg,#1e8f3e,#eea22a);opacity:.6;border-radius:12px}
.products-title{left:624px;top:813px}
.products-rule{left:81px;top:827px;width:522px;height:1px;background:var(--rule)}
.florist-photo{left:81px;top:859px;width:273px;height:249px;border-radius:3px;background:linear-gradient(160deg,#d8cfc8,#9a3a3a 50%,#e04a3a 85%)}
.dots{left:62px;top:964px;display:flex;flex-direction:column;gap:5px}
.dots span{width:5px;height:5px;border:1px solid var(--orange);border-radius:50%}
.dots span.on{width:7px;height:7px;margin-left:-1px;background:var(--orange)}
.products-text{left:371px;top:864px;width:362px}
.product{position:absolute;top:971px;width:80px;transform:translateX(-50%);text-align:center}
.product .thumb{width:51px;height:51px;border-radius:50%;margin:0 auto 8px}
.product .name{font-size:8.5px;font-weight:500}
.product .price{font-size:7px;color:var(--muted);margin-top:3px}
</style>
</head>
<body>
<svg class="icon" style="left:82px;top:23px" viewBox="0 0 16 16" fill="none" stroke="#555" stroke-width="1.6"><circle cx="6.5" cy="6.5" r="5"/><line x1="10.3" y1="10.3" x2="14.5" y2="14.5"/></svg>
<div class="brand"><span class="brand-dot"></span><span class="brand-name">Sparrowgate Petals</span></div>
<svg class="icon" style="left:711px;top:22px" viewBox="0 0 16 18" fill="none" stroke="#555" stroke-width="1.3"><rect x="2" y="5" width="12" height="12" rx="1"/><path d="M5.5 5V3.5a2.5 2.5 0 0 1 5 0V5"/><path d="M6 9a2 2 0 0 0 4 0"/></svg>
<div class="abs nav-rule"></div>
<nav class="nav">
  <a style="left:258px">About Us</a>
  <a style="left:350px">For Supermarkets</a>
  <a style="left:456px">For Franchisees</a>
  <a style="left:548px">Contact Us</a>
</nav>

<div class="photo hero-photo" role="img" aria-label="Wrapped bouquet of red and orange roses with yellow filler flowers"></div>
<div class="photo deco-right" role="img" aria-label="Decorative cut flowers at the page edge"></div>
<div class="photo bee-trail" role="img" aria-label="Decorative bee with dashed flight trail"></div>
<h1 class="abs hero-title">FLOWERS<br>BOUQUETS</h1>
<div class="btn" style="left:88px;top:310px">Order Now</div>
<p class="abs hero-note">Fresh flowers convey beauty and love, and in our view should become something every person regularly enjoys.</p>
<div class="photo hero-circle" role="img" aria-label="Hands tying a ribbon around a mixed bouquet"></div>

<h2 class="abs section-title about-title">About Us</h2>
<div class="abs about-rule"></div>
<div class="abs next-btn"><svg width="14" height="10" viewBox="0 0 14 10" fill="none" stroke="#1e8f3e" stroke-width="1.3"><line x1="1" y1="5" x2="13" y2="5"/><path d="M9 1l4 4-4 4"/></svg></div>
<div class="photo about-photo-a" role="img" aria-label="Florist trimming stems of a pink and green bouquet"></div>
<div class="photo about-photo-b" role="img" aria-label="Supermarket floral display with baskets and price tags"></div>
<p class="abs body-text about-text"><strong>Fresh Flowers</strong> convey beauty and love, and in our view should become something every person regularly enjoys.&nbsp; Sparrowgate Petals is an entrepreneurial company created to make top quality fresh flowers and professionally-designed bouquets accessible to every consumer at affordable prices.</p>
<div class="photo deco-left" role="img" aria-label="Decorative pink petunias at the page edge"></div>

<div class="photo bee-mark" role="img" aria-label="Small decorative bee"></div>
<h2 class="abs section-title products-title">Products</h2>
<div class="abs products-rule"></div>
<div class="photo florist-photo" role="img" aria-label="Smiling florist in an apron holding a bouquet in a flower shop"></div>
<div class="abs dots"><span></span><span></span><span></span><span class="on"></span></div>
<p class="abs body-text products-text"><strong>Professional Florists</strong> typically sell the finest quality stems, design the most beautiful bouquets and provide the finest customer service, but their costs – of floral products, retail spaces, labor and marketing – force them to pass high prices along to customers. Supermarket flower departments benefit from high customer footfall, economies of scale and low pricing, but their quality of stems and bouquets is typically poor, staffing is limited, and staff turnover is high which can result in inefficiency, wastage, poorly merchandised selections and limited service.</p>

<div class="product" style="left:396px"><div class="thumb" role="img" aria-label="Florist holding a basket of flowers" style="background:radial-gradient(circle,#c88a6a,#3a5a7a)"></div><div class="name">Cannas</div><div class="price">$95.00</div></div>
<div class="product" style="left:500px"><div class="thumb" role="img" aria-label="Red roses" style="background:radial-gradient(circle,#d8202a,#1e5a2a)"></div><div class="name">Rose</div><div class="price">$85.00</div></div>
<div class="product" style="left:603px"><div class="thumb" role="img" aria-label="Mixed pink bouquet" style="background:radial-gradient(circle,#e07a9a,#6a8a5a)"></div><div class="name">Broome</div><div class="price">$75.00</div></div>
<div class="product" style="left:705px"><div class="thumb" role="img" aria-label="Flower basket display" style="background:radial-gradient(circle,#e0402a,#3a4a3a)"></div><div class="name">Libra</div><div class="price">$88.00</div></div>
<div class="btn" style="left:371px;top:1070px">Order Now</div>
</body>
</html>
```